Fall Convention Graphic Designs (logo, digital brochure, t-shirt designs, social media templates)

I need a graphic package for the Bellrose Motion Guild Fall Dance Convention. Bellrose Motion Guild is a non-profit organization of dance teachers, and this educational dance conference is for members and their students with multiple events throughout the weekend. The convention has a new them each year. I will need a package with a general "logo" type graphic, a digital brochure, t-shirt design, and social media graphic templates. This year's Convention has a general theme and names for each event throughout the weekend.
The theme and event names for this year are:
Convention Theme Twice Around a Tune: Beneath the Harbor Moon
Registration Desk The Compass Nook
Members Welcome A Moonbeam Greeting
Banquet A Velvet Twilight
President's Reception Raise Every Glass
Jr. Member Desk Wanderers' Wharf
Jr. Member Pizza Party Cricket Mixer
Members Luncheon Meadow Reveries

I am attaching a word file that includes information and text to be included in brochure. Also attached are designs from previous years for brochures, T-shirts, and social media graphics.

Colors that we will be using for decorations at various events over the weekend this year are shades of green (fern and mossy green), shades of blue (including navy), white, and pinks (including mauve). The banquet event will be decorated as an enchanted forest. We are using fairy lights, books that look like a storybook, and lanterns for decorations as well. I think I would like a more modern design, and I do not want anything that is childish or too whimsical. While we are using floral decorations I don't want bunches of flowers in the design.

*I am open to seeing initial logo type designs and giving feedback to make sure it is a direction that I like and then moving forward with the other parts of the project.

```html
<!DOCTYPE html>
<html lang="en">
<head>
<meta charset="utf-8">
<title>Bellrose Motion Guild Fall Convention – Initial Proposal</title>
<link rel="stylesheet" href="https://fonts.googleapis.com/css2?family=Poppins:wght@400;600&family=Oswald:wght@300;400&family=Mr+Dafoe&display=swap">
<style>
  :root {
    --stage: #676767;
    --ink-light: #f2f2f2;
    --frame-line: #a9a9a9;
    --night: #000000;
    --navy: #0b1f4a;
    --aurora-blue: #1c6fa0;
    --aurora-teal: #2ad6a5;
    --mint: #3df5bd;
    --glow: #4fe0d0;
    --deep-ink: #0b2a3a;
    --white: #ffffff;
  }
  * { box-sizing: border-box; margin: 0; padding: 0; }
  html, body {
    width: 1200px; height: 930px; overflow: hidden;
    background: var(--stage);
  }
  .canvas { position: relative; width: 1200px; height: 930px; }

  .proposal-note {
    position: absolute; left: 138px; top: 58px; width: 736px; height: 81px;
    border: 1px solid var(--frame-line);
    padding: 13px 15px;
    font-family: "Poppins", sans-serif; color: var(--ink-light);
  }
  .proposal-note__label { font-weight: 600; font-size: 15px; line-height: 20px; }
  .proposal-note__text { font-weight: 400; font-size: 15px; line-height: 20px; margin-top: 9px; }

  .night-scene {
    position: absolute; inset: 0;
    background: linear-gradient(to bottom,
      var(--night) 0%, var(--night) 48%,
      var(--navy) 58%, var(--aurora-blue) 68%,
      var(--aurora-teal) 78%, var(--mint) 86%, var(--mint) 100%);
  }

  .poster {
    position: absolute; left: 140px; top: 170px; width: 522px; height: 695px;
    overflow: hidden;
  }
  .poster__host {
    position: absolute; top: 24px; left: 0; right: 0; text-align: center;
    font-family: "Oswald", sans-serif; font-weight: 300; color: var(--white);
    font-size: 19px; line-height: 25px; letter-spacing: 0.3em;
  }
  .theme-title {
    position: absolute; left: 0; right: 0; text-align: center;
    font-family: "Mr Dafoe", cursive; font-weight: 400; color: var(--white);
    white-space: nowrap;
    text-shadow: 0 0 4px var(--glow), 0 0 10px var(--glow);
  }
  .theme-title span { display: block; }
  .poster .theme-title { top: 158px; }
  .poster .theme-title__lead { font-size: 46px; line-height: 60px; padding-left: 40px; }
  .poster .theme-title__main { font-size: 60px; line-height: 72px; }

  .poster__details {
    position: absolute; left: 0; right: 0; top: 600px; text-align: center;
    font-family: "Oswald", sans-serif; font-weight: 300; color: var(--deep-ink);
    font-size: 20px; line-height: 21.5px;
  }
  .poster__city { display: flex; align-items: center; justify-content: center; gap: 8px; }
  .poster__city::before, .poster__city::after {
    content: ""; width: 138px; height: 1px; background: var(--deep-ink);
  }

  .badge {
    position: absolute; left: 711px; top: 342px; width: 350px; height: 350px;
    border-radius: 50%; overflow: hidden;
  }
  .badge .night-scene {
    background: linear-gradient(to bottom,
      var(--night) 0%, var(--night) 42%,
      var(--navy) 54%, var(--aurora-blue) 64%,
      var(--aurora-teal) 78%, var(--mint) 92%, var(--mint) 100%);
  }
  .badge .theme-title { top: 48px; }
  .badge .theme-title__lead { font-size: 30px; line-height: 44px; padding-left: 24px; }
  .badge .theme-title__main { font-size: 40px; line-height: 50px; }
</style>
</head>
<body>
<main class="canvas">
  <section class="proposal-note">
    <p class="proposal-note__label">INITIAL PROPOSAL:</p>
    <p class="proposal-note__text">for the graphic package for the Bellrose Motion Guild Fall Dance Convention.</p>
  </section>

  <article class="poster">
    <div class="night-scene" role="img" aria-label="Starry night sky with teal aurora over dark mountains and a pine forest"></div>
    <p class="poster__host">BELLROSE MOTION GUILD, INC.<br>FALL CONVENTION</p>
    <h1 class="theme-title">
      <span class="theme-title__lead">Twice Around a Tune:</span>
      <span class="theme-title__main">Beneath the Harbor</span>
      <span class="theme-title__main">Moon</span>
    </h1>
    <div class="poster__details">
      <p>November 19 – 22, 2026</p>
      <p>Alder Hall Convention Center</p>
      <p>Harborline Grand Hotel</p>
      <p class="poster__city">Marlow Bay, NC</p>
    </div>
  </article>

  <aside class="badge">
    <div class="night-scene" role="img" aria-label="Starry night sky with teal aurora over dark mountains and a pine forest"></div>
    <h2 class="theme-title">
      <span class="theme-title__lead">Twice Around a Tune:</span>
      <span class="theme-title__main">Beneath the Harbor</span>
      <span class="theme-title__main">Moon</span>
    </h2>
  </aside>
</main>
</body>
</html>
```